Banner design for Quillmere & Dastow Chamber of Commerce

We would like a design for banners that will hang in the towns of Quillmere & Dastow located in southwestern Ontario, Canada. We have some specific things that need to be included on the banner.

The logo from our website must appear at the top of the banner using the logo and same colours. i.e. Quillmere in white lettering, green background. See logo and colour specifics that have been provided in digital form.

There is one addition we would like in the logo. Below "Visit Quillmere" and above the tag line "a great place to grow" we want to add "& Dastow" using one of the two fonts already being used in the logo.

At the bottom of the banner (against the green colour) we would like it to read: Chamber of Commerce on one line and below this the web address, www.visitquillmere.ca

The space on the banner in between the top and the bottom of the banner we would like to see images that include the following representations: 1. Wine/glasses of wine/grapes/vineyards (vineyards should reflect the Lake Erie North Shore wine region) 2. Industry (we have many large industries in our town) including Pendry Forge, Norcavan Equipment, Vultaray, Brightmoss Fuel, possibly these could be represented by a single image representing industry. 3. Agriculture keep in mind that we are located in southwestern Ontario and we would like the image(s) to reflective of our agricultural area. We are also known for our greenhouse technology in our region and we grow tomatoes, corn, soybeans, cucumbers, peppers, asparagus and we also have orchards of apples, pears, and peaches. 4. Dastow harbour located on the north shore of Lake Erie in the village of Dastow. These are listed in order of importance, and so the size and frequency of the images should reflect this. The wineries located in Quillmere and Dastow represent the most important tourism attraction in our towns.

These banners will be placed in both the towns of Quillmere and Dastow along the main entrances and thoroughfares. These vertical banners will be seen as visitors enter our town(s). We want them to be colourful and beautiful/elegant; but easily recognizable and easily read by passing motorists.

See also http://explorebravlenmoor.com/ for ideas.

The dimensions for the banners are: 60" in height and 24" in width.

Please provide us with digital files that are print ready.

Thank you,
Cheers,
Marisol Tebbet
Director Quillmere & Dastow Chamber of Commerce

Target Market(s)

Tourists, potential business investors

Industry/Entity Type

Chamber Of Commerce

Font styles to use
Other font styles liked:
• The font(s) used in our existing logo, file is provided

Requirements
Must have
• Must be designed to fit dimensions for banner. See project description for other must haves.
Nice to have
• See project description.
Should not have
• Should not have images that do not reflect our region of southwestern Ontario.

```html
<!DOCTYPE html>
<html lang="en">
<head>
<meta charset="utf-8">
<title>Visit Quillmere &amp; Dastow – Street Banner</title>
<link href="https://fonts.googleapis.com/css2?family=Arimo:wght@400;700&display=swap" rel="stylesheet">
<style>
  :root {
    --green: #6cb33f;
    --purple: #7a51a6;
    --blue: #219bd8;
    --ink: #2e2e2e;
    --frame: #4a4a4a;
    --white: #ffffff;
    --page: #ffffff;
    --dim: #d9322b;
  }
  * { box-sizing: border-box; margin: 0; padding: 0; }
  html, body { width: 1200px; height: 1000px; overflow: hidden; background: var(--page); }
  body { position: relative; font-family: 'Arimo', Arial, sans-serif; }

  .dimension { position: absolute; }
  .dimension-width { left: 417px; top: 28px; width: 366px; height: 12px; border-top: 1px solid var(--dim); }
  .dimension-width::before, .dimension-width::after,
  .dimension-height::before, .dimension-height::after { content: ""; position: absolute; background: var(--dim); }
  .dimension-width::before { left: 0; top: -6px; width: 1px; height: 12px; }
  .dimension-width::after { right: 0; top: -6px; width: 1px; height: 12px; }
  .dimension-width span { position: absolute; top: -14px; left: 0; right: 0; text-align: center; font-size: 8px; color: var(--dim); }
  .dimension-height { left: 398px; top: 45px; width: 12px; height: 910px; border-left: 1px solid var(--dim); }
  .dimension-height::before { top: 0; left: -6px; width: 12px; height: 1px; }
  .dimension-height::after { bottom: 0; left: -6px; width: 12px; height: 1px; }
  .dimension-height span { position: absolute; top: 455px; left: -30px; transform: rotate(-90deg); font-size: 8px; color: var(--dim); white-space: nowrap; }

  .banner {
    position: absolute; left: 417px; top: 45px; width: 366px; height: 910px;
    border: 2px solid var(--frame); background: var(--white);
    display: grid; grid-template-rows: 133px repeat(5, auto) 1fr; row-gap: 4px;
  }
  .banner-header {
    background: var(--green); text-align: center; color: var(--white);
    display: flex; flex-direction: column; align-items: center; justify-content: center;
  }
  .brand-name { font-size: 38px; font-weight: 700; letter-spacing: 1px; line-height: 1.1; }
  .brand-second { font-size: 19px; letter-spacing: 4px; margin-top: 4px; }
  .tagline { font-size: 18px; letter-spacing: 3px; color: var(--ink); margin-top: 4px; }

  .tile-row { display: grid; grid-template-columns: 181px 1fr; column-gap: 3px; }
  .row-1 { height: 128px; } .row-2 { height: 133px; } .row-3 { height: 132px; }
  .row-4 { height: 145px; } .row-5 { height: 136px; }

  .photo { width: 100%; height: 100%; }
  .photo-canola { background: linear-gradient(180deg, #4d8fd8 0%, #a9cdf0 45%, #e8d01c 58%, #c9b50c 100%); }
  .photo-vineyard { background: linear-gradient(160deg, #e07a1c 0%, #f2a43a 35%, #7f9a2a 65%, #3f5a14 100%); }
  .photo-lake { background: linear-gradient(180deg, #9ec4e6 0%, #2f6b2a 30%, #3c7d36 60%, #5a93b4 80%, #9a8a6a 100%); }
  .photo-wine-pour { background: radial-gradient(circle at 35% 70%, #8c0f16 0%, #b5222a 25%, #f1d9a8 60%, #e6b66c 100%); }
  .photo-orchard { background: linear-gradient(180deg, #3f6b1e 0%, #5f8f2a 50%, #b22a1e 75%, #6b8a32 100%); }
  .photo-mill { background: linear-gradient(180deg, #3d86d6 0%, #a8c9ea 30%, #d6c29a 45%, #b39c72 85%, #6c5b45 100%); }
  .photo-hay { background: linear-gradient(180deg, #d8e6f0 0%, #6a8f3a 18%, #d9a648 40%, #b8822c 100%); }

  .category {
    display: flex; flex-direction: column; align-items: center; justify-content: center;
    color: var(--white); text-align: center; font-size: 16px; line-height: 1.15;
  }
  .category-tourism { background: var(--green); }
  .category-wine { background: var(--purple); }
  .category-industry { background: var(--blue); font-size: 18px; }
  .category svg { margin-bottom: 6px; }

  .banner-footer {
    background: var(--green); text-align: center;
    display: flex; flex-direction: column; justify-content: center;
  }
  .footer-title { color: var(--white); font-size: 24px; letter-spacing: 1.5px; }
  .footer-url { color: var(--ink); font-size: 11px; letter-spacing: 3.5px; margin-top: 10px; }
</style>
</head>
<body>
  <div class="dimension dimension-width"><span>24" in Width</span></div>
  <div class="dimension dimension-height"><span>60" in Height</span></div>

  <main class="banner">
    <header class="banner-header">
      <div class="brand-name">Visit Quillmere</div>
      <div class="brand-second">&amp; DASTOW</div>
      <div class="tagline">a great place to grow</div>
    </header>

    <section class="tile-row row-1">
      <div class="photo photo-canola" role="img" aria-label="Red barn beyond a yellow canola field under blue sky"></div>
      <div class="photo photo-vineyard" role="img" aria-label="Bottle and glass of white wine with grapes before a sunset vineyard"></div>
    </section>

    <section class="tile-row row-2">
      <div class="photo photo-lake" role="img" aria-label="Lakeside cottage among pine trees with a wooden dock"></div>
      <div class="category category-tourism">
        <svg width="90" height="40" viewBox="0 0 90 40" aria-hidden="true">
          <path d="M18 4 L18 30 L4 30 Z" fill="#fff"/>
          <path d="M21 8 L21 30 L34 30 Z" fill="#fff"/>
          <path d="M2 32 L38 32 L33 38 L7 38 Z" fill="#fff"/>
          <g fill="none" stroke="#fff" stroke-width="2">
            <circle cx="46" cy="30" r="7"/><circle cx="68" cy="30" r="7"/>
            <path d="M46 30 L53 20 L64 20 L68 30 M53 20 L57 30 L64 20 M52 17 L56 17 M63 20 L62 15 L66 15"/>
          </g>
          <rect x="76" y="20" width="11" height="14" fill="#fff"/>
          <path d="M79 20 V17 H84 V20" fill="none" stroke="#fff" stroke-width="1.5"/>
        </svg>
        <div>Tourism, Nature<br>&amp; Shopping</div>
      </div>
    </section>

    <section class="tile-row row-3">
      <div class="category category-wine">
        <svg width="34" height="42" viewBox="0 0 34 42" aria-hidden="true" fill="#fff">
          <path d="M18 10 C20 3 26 1 30 2 C28 7 24 10 18 10 Z"/>
          <circle cx="9" cy="15" r="3.6"/><circle cx="17" cy="15" r="3.6"/><circle cx="25" cy="15" r="3.6"/>
          <circle cx="13" cy="22" r="3.6"/><circle cx="21" cy="22" r="3.6"/>
          <circle cx="9" cy="29" r="3.6" opacity="0"/><circle cx="17" cy="29" r="3.6"/>
          <circle cx="13" cy="35" r="3.2" opacity="0"/><circle cx="17" cy="36" r="3.2"/>
        </svg>
        <div>Wineries<br>&amp; Vineyards</div>
      </div>
      <div class="photo photo-wine-pour" role="img" aria-label="Red wine being poured into two glasses"></div>
    </section>

    <section class="tile-row row-4">
      <div class="photo photo-orchard" role="img" aria-label="Apple orchard with red apples, ladder and baskets"></div>
      <div class="photo photo-mill" role="img" aria-label="Historic brick grain mill building with a vintage truck"></div>
    </section>

    <section class="tile-row row-5">
      <div class="photo photo-hay" role="img" aria-label="Round hay bales on a golden harvested field"></div>
      <div class="category category-industry">
        <svg width="64" height="44" viewBox="0 0 64 44" aria-hidden="true">
          <g fill="none" stroke="#fff">
            <circle cx="20" cy="18" r="10" stroke-width="5" stroke-dasharray="4 3"/>
            <circle cx="20" cy="18" r="6" stroke-width="4"/>
            <circle cx="42" cy="28" r="11" stroke-width="5" stroke-dasharray="4 3"/>
            <circle cx="42" cy="28" r="7" stroke-width="4"/>
          </g>
        </svg>
        <div>Agriculture<br>&amp; Industries</div>
      </div>
    </section>

    <footer class="banner-footer">
      <div class="footer-title">Chamber of Commerce</div>
      <div class="footer-url">www.visitquillmere.ca</div>
    </footer>
  </main>
</body>
</html>
```